Torvane PT Business Card

I need the card to be bright/bold colours to stand out amongst others.
It needs to have my company logo.
I was not interested in pictures etc just a layout that attracts attention.

I have attached my old design which is very plain. I also needed change the contact details. And my description changed to Personal Trainer
Phone 0427309581
Facebook Torvane PT
No email address please, no street address.
And only Torvane PT (Please remove anything to do with Torvane Supplements)

```html
<!DOCTYPE html>
<html lang="en">
<head>
<meta charset="UTF-8">
<title>Torvane PT – Business Card</title>
<link rel="stylesheet" href="https://fonts.googleapis.com/css2?family=Montserrat:wght@800&family=Lato:wght@400&display=swap">
<style>
  :root {
    --page-bg: #e9ecee;
    --card-bg: #222325;
    --panel-light: #f3f5f6;
    --brand-yellow: #f6cf1c;
    --text-white: #ffffff;
    --text-soft: #e6e6e6;
  }
  * { margin: 0; padding: 0; box-sizing: border-box; }
  html, body {
    width: 1200px;
    height: 900px;
    overflow: hidden;
    background: var(--page-bg);
  }
  .canvas {
    position: relative;
    width: 1200px;
    height: 900px;
  }
  .business-card {
    position: absolute;
    left: 226px;
    top: 236px;
    width: 748px;
    height: 428px;
    background: var(--card-bg);
    box-shadow: 0 6px 24px rgba(0, 0, 0, 0.18);
    overflow: hidden;
  }
  .side-panel {
    position: absolute;
    left: 0;
    top: 0;
    width: 220px;
    height: 428px;
  }
  .brand-name {
    position: absolute;
    left: 182px;
    top: 58px;
    font-family: "Montserrat", sans-serif;
    font-weight: 800;
    font-size: 44px;
    letter-spacing: 1px;
    color: var(--brand-yellow);
    line-height: 1;
  }
  .contact-block {
    position: absolute;
    left: 446px;
    top: 218px;
  }
  .person-name {
    font-family: "Montserrat", sans-serif;
    font-weight: 800;
    font-size: 35px;
    line-height: 1;
    color: var(--text-white);
    letter-spacing: 0.5px;
  }
  .person-name .surname { color: var(--brand-yellow); }
  .person-role {
    margin-top: 2px;
    font-family: "Lato", sans-serif;
    font-size: 26px;
    line-height: 1.2;
    color: var(--text-soft);
  }
  .contact-list {
    list-style: none;
    margin-top: 14px;
  }
  .contact-item {
    display: flex;
    align-items: center;
    gap: 10px;
    height: 34px;
    font-family: "Lato", sans-serif;
    font-size: 20px;
    color: var(--text-white);
  }
  .contact-icon {
    width: 26px;
    height: 26px;
    flex: none;
  }
</style>
</head>
<body>
  <main class="canvas">
    <section class="business-card" aria-label="Torvane PT business card">
      <svg class="side-panel" viewBox="0 0 220 428" role="img" aria-label="Light brand decoration area along the left edge">
        <path d="M0 0 H125 C150 120 150 330 205 428 H0 Z" fill="var(--panel-light)"/>
      </svg>

      <div class="brand-name">TORVANE PT</div>

      <div class="contact-block">
        <h1 class="person-name">DANA <span class="surname">MARSH</span></h1>
        <p class="person-role">Personal Trainer</p>
        <ul class="contact-list">
          <li class="contact-item">
            <svg class="contact-icon" viewBox="0 0 26 26" aria-hidden="true">
              <circle cx="13" cy="13" r="13" fill="var(--brand-yellow)"/>
              <path d="M7 10.5c0-1.6 2.6-2.8 6-2.8s6 1.2 6 2.8v1h-2.6v-1.4c-1-.4-2.1-.6-3.4-.6s-2.4.2-3.4.6v1.4H7z M9 12.5h8l1.5 5h-11z" fill="var(--card-bg)"/>
              <circle cx="13" cy="15" r="1.4" fill="var(--brand-yellow)"/>
            </svg>
            <span>0427 309 581</span>
          </li>
          <li class="contact-item">
            <svg class="contact-icon" viewBox="0 0 26 26" aria-hidden="true">
              <circle cx="13" cy="13" r="13" fill="var(--brand-yellow)"/>
            </svg>
            <span>Torvane PT</span>
          </li>
        </ul>
      </div>
    </section>
  </main>
</body>
</html>
```